Checkout sign

Wall sign for clinic checkout.
“The Good Lord does ALL the healing..
But we DO collect the co-pay”

Add Celtic cross at top and our logo on bottom

```html
<!DOCTYPE html>
<html lang="en">
<head>
<meta charset="utf-8">
<title>Checkout Sign – Halloran Orthopedic Clinic</title>
<link href="https://fonts.googleapis.com/css2?family=Cinzel:wght@400;600;700&display=swap" rel="stylesheet">
<style>
  :root {
    --royal: #1a0090;
    --slate: #5b5b5b;
    --paper: #ffffff;
    --backdrop: #e4e4e4;
  }
  html, body {
    margin: 0;
    padding: 0;
    width: 1200px;
    height: 1200px;
    overflow: hidden;
    background: var(--backdrop);
  }
  .stage {
    position: relative;
    width: 1200px;
    height: 1200px;
  }
  .sign-frame {
    position: absolute;
    left: 200px;
    top: 40px;
    width: 799px;
    height: 1120px;
    overflow: hidden;
  }
  .sign {
    position: absolute;
    left: 0;
    top: 0;
    width: 1162px;
    height: 1628px;
    background: var(--paper);
    transform: scale(0.6876);
    transform-origin: 0 0;
    font-family: "Cinzel", serif;
  }
  .sign svg { position: absolute; left: 0; top: 0; }
  .line {
    position: absolute;
    left: 0;
    width: 100%;
    margin: 0;
    text-align: center;
    line-height: 1;
    white-space: nowrap;
  }
  .line--lord   { top: 598px; font-size: 68px; font-weight: 700; color: var(--royal); }
  .line--healing{ top: 684px; font-size: 64px; font-weight: 400; color: var(--slate); text-transform: lowercase; font-variant: small-caps; }
  .line--collect{ top: 766px; font-size: 64px; font-weight: 400; color: var(--slate); }
  .line--copay  { top: 849px; font-size: 62px; font-weight: 700; color: var(--slate); }
  .caps { text-transform: uppercase; }
  .clinic-name {
    position: absolute;
    left: 0;
    width: 100%;
    text-align: center;
    color: var(--paper);
    font-weight: 400;
    line-height: 1;
  }
  .clinic-name__main { top: 1472px; font-size: 72px; }
  .clinic-name__sub  { top: 1541px; font-size: 34px; letter-spacing: 0.02em; }
</style>
</head>
<body>
<main class="stage">
  <div class="sign-frame">
    <article class="sign">
      <svg width="1162" height="1628" viewBox="0 0 1162 1628" aria-hidden="false">
        <g class="celtic-cross" role="img" aria-label="Celtic cross with interlaced knotwork">
          <path fill="var(--royal)" d="M497 76 H665 V235 H823 V403 H665 V562 H497 V403 H339 V235 H497 Z"/>
        </g>
        <path class="wave-band" fill="var(--royal)"
          d="M0 908 C300 860 600 1000 850 1040 C1000 1062 1100 965 1162 913 L1162 1628 L0 1628 Z"/>
        <path class="wave-stripe" fill="var(--paper)"
          d="M0 1000 C250 930 550 1020 850 1100 C1000 1140 1100 1060 1162 1000 C1080 1090 950 1140 800 1130 C550 1100 300 960 0 1000 Z"/>
        <path class="wave-stripe" fill="var(--paper)"
          d="M170 1080 C400 1030 600 1150 800 1195 C880 1210 950 1170 995 1128 C920 1190 830 1215 760 1205 C550 1175 400 1040 170 1080 Z"/>
        <circle class="clinic-mark" cx="581" cy="1350" r="100" fill="none" stroke="var(--paper)" stroke-width="6"/>
      </svg>

      <p class="line line--lord">The Good Lord</p>
      <p class="line line--healing">does <span class="caps">ALL</span> the healing..</p>
      <p class="line line--collect">But we DO collect</p>
      <p class="line line--copay">THE CO-PAY</p>

      <div class="clinic-name clinic-name__main">Halloran</div>
      <div class="clinic-name clinic-name__sub">Orthopedic Clinic</div>
    </article>
  </div>
</main>
</body>
</html>
```